Cryptocurrency Advisor Business Card

Velbridge Consulting Services is my company, which advises many projects in the ICO/Cryptocurrency industry. I'd like to get a sleek, preferably matte black or matte dark blue finish, business card with the company name (and simple logo w/ crypto feel) on one side and while the other side I'd like a small twitter and telegram logo together maybe separated by a / as it's the same, then an email and a phone logo so I can insert those specifics there (no address). Can have name then CEO section too. At the bottom of that section, find a place for more of a job description: ICO Advisor, World Champion Gamer, Esports Award Winner, Varlomark Expert. You can possibly design a simple logo or use something with a crypto twist or background, but nothing too complex. Rounded edges for printing not square.
Updates

Had personal issues taking a few days away from me being able to provide feedback and check designs, etc. Will be more active now finalizing design just needed few days from issue but all is sorted.

Target Market(s)

Cryptocurrency industry

Industry/Entity Type

Management Consulting

Contact Information for Business Card

Font styles to use
Sans Serif

Colors
5c5c5c
474747
757575
9d9d9d
aaaaaa
333333
0355a3

Requirements
Must have
• Refer to Details/Description
Nice to have
Should not have
• Address section

```html
<!DOCTYPE html>
<html lang="en">
<head>
<meta charset="utf-8">
<title>Velbridge Consulting Services – Business Card</title>
<link href="https://fonts.googleapis.com/css2?family=Montserrat:wght@600&family=Roboto:wght@400&family=Roboto+Condensed:wght@400&display=swap" rel="stylesheet">
<style>
  :root {
    --brand-blue: #0355a3;
    --ink-dark: #333333;
    --ink-mid: #474747;
    --ink-soft: #5c5c5c;
    --paper: #ffffff;
    --backdrop: #2a2a2a;
  }
  * { margin: 0; padding: 0; box-sizing: border-box; }
  html, body { width: 1200px; height: 930px; overflow: hidden; }
  body { background: var(--backdrop); position: relative; font-family: "Roboto", sans-serif; }

  .card {
    position: absolute;
    width: 600px; height: 343px;
    border-radius: 14px;
    overflow: hidden;
  }

  /* Front */
  .card-front { left: 80px; top: 90px; background: var(--brand-blue); color: var(--paper); }
  .card-front .brand { position: absolute; left: 175px; top: 120px; }
  .card-front .tagline {
    position: absolute; left: 24px; bottom: 20px;
    font-family: "Roboto Condensed", sans-serif;
    font-size: 13.5px; letter-spacing: 0.2px; text-transform: uppercase;
  }

  .brand { display: flex; align-items: center; gap: 14px; }
  .brand-mark { width: 58px; height: 58px; border-radius: 50%; flex: none; }
  .brand-name {
    font-family: "Montserrat", sans-serif; font-weight: 600;
    line-height: 1.1;
  }
  .brand-name .primary { display: block; font-size: 34px; }
  .brand-name .secondary { display: block; font-size: 19px; }
  .card-front .brand-mark { background: var(--paper); }
  .card-front .brand-name { color: var(--paper); }

  /* Back */
  .card-back { left: 520px; top: 497px; background: var(--paper); }
  .card-back .brand { position: absolute; left: 38px; top: 150px; }
  .card-back .brand-mark { background: var(--brand-blue); width: 50px; height: 50px; }
  .card-back .brand-name { color: var(--brand-blue); }
  .card-back .brand-name .primary { font-size: 29px; }
  .card-back .brand-name .secondary { font-size: 16px; }

  .divider { position: absolute; left: 300px; top: 82px; width: 2px; height: 150px; background: var(--brand-blue); }

  .contact { position: absolute; left: 322px; top: 74px; color: var(--ink-dark); }
  .contact .person-name { font-size: 24px; color: var(--brand-blue); text-transform: uppercase; letter-spacing: 0.3px; }
  .contact .person-role { font-size: 14px; color: var(--ink-mid); margin-bottom: 10px; }
  .contact ul { list-style: none; }
  .contact li { display: flex; align-items: center; gap: 9px; font-size: 15px; line-height: 21px; }
  .contact li.gap-before { margin-top: 10px; }
  .contact svg { width: 11px; height: 11px; flex: none; }
  .social-dot { width: 10px; height: 10px; border-radius: 50%; background: var(--brand-blue); flex: none; }

  .band-dark { position: absolute; left: 0; bottom: 0; width: 370px; height: 14px; background: var(--ink-dark); }
  .band-blue { position: absolute; left: 372px; bottom: 14px; right: 0; height: 10px; background: var(--brand-blue); }
</style>
</head>
<body>

<section class="card card-front" aria-label="Business card front">
  <div class="brand">
    <span class="brand-mark"></span>
    <span class="brand-name"><span class="primary">Velbridge</span><span class="secondary">Consulting Services</span></span>
  </div>
  <p class="tagline">ICO Advisor - World Champion Gamer - Esports Award Winner - Varlomark Expert.</p>
</section>

<section class="card card-back" aria-label="Business card back">
  <div class="brand">
    <span class="brand-mark"></span>
    <span class="brand-name"><span class="primary">Velbridge</span><span class="secondary">Consulting Services</span></span>
  </div>
  <div class="divider"></div>
  <div class="contact">
    <p class="person-name">Elias Brandt</p>
    <p class="person-role">CEO</p>
    <ul>
      <li><svg viewBox="0 0 24 24"><path fill="#0355a3" d="M6.6 10.8a15 15 0 0 0 6.6 6.6l2.2-2.2a1 1 0 0 1 1-.25 11.4 11.4 0 0 0 3.6.57 1 1 0 0 1 1 1V20a1 1 0 0 1-1 1A17 17 0 0 1 3 4a1 1 0 0 1 1-1h3.5a1 1 0 0 1 1 1c0 1.25.2 2.45.57 3.57a1 1 0 0 1-.25 1z"/></svg>+330 5550-1927</li>
      <li><svg viewBox="0 0 24 24"><rect x="2" y="5" width="20" height="14" rx="2" fill="none" stroke="#0355a3" stroke-width="2.5"/><path d="M3 6l9 7 9-7" fill="none" stroke="#0355a3" stroke-width="2.5"/></svg>elias@velbridge.com</li>
      <li><svg viewBox="0 0 24 24"><circle cx="12" cy="12" r="10" fill="none" stroke="#0355a3" stroke-width="2"/><path d="M2 12h20M12 2c3 3 3 17 0 20M12 2c-3 3-3 17 0 20" fill="none" stroke="#0355a3" stroke-width="2"/></svg>velbridgeconsulting.com</li>
      <li class="gap-before"><span class="social-dot"></span>555 010 234</li>
      <li><span class="social-dot"></span>@velbridgeconsult</li>
    </ul>
  </div>
  <div class="band-dark"></div>
  <div class="band-blue"></div>
</section>

</body>
</html>
```